WRM Marketing Postcard

Design a 2 Sided marketing postcard for our Real estate management caompany. Looking for a professional yet fresh look that will be printed on a 6"x9" glossy flier

Contact information is www.wexleymanagement.com wexleymanagement@inboxvane.com and 312-555-0187

WE are targeting small condo and town home properties to take on their administrative responsibilities of management

```html
<!DOCTYPE html>
<html lang="en">
<head>
<meta charset="utf-8">
<title>WRM Marketing Postcard</title>
<link rel="stylesheet" href="https://fonts.googleapis.com/css2?family=Lato:wght@400;700&family=Montserrat:wght@700;800&display=swap">
<style>
  :root {
    --brand-blue: #1a77b2;
    --page-bg: #b9b8b9;
    --card-white: #ffffff;
    --text-gray: #555555;
    --head-light: #e3e3e3;
    --head-dark: #b2b2b2;
    --head-text: #8a8a8a;
    --row-tint: #f6f6f6;
    --rule: #e6e6e6;
    --stamp: #e4e4e4;
  }
  * { box-sizing: border-box; margin: 0; padding: 0; }
  html, body { width: 1200px; height: 1200px; overflow: hidden; }
  body {
    background: var(--page-bg);
    font-family: "Lato", sans-serif;
    color: var(--text-gray);
    display: flex; flex-direction: column; align-items: center;
    gap: 40px; padding-top: 20px;
  }
  .postcard {
    position: relative; width: 840px; height: 560px;
    background: var(--card-white);
    box-shadow: 0 2px 6px rgba(0,0,0,.18);
    overflow: hidden;
  }

  /* front */
  .front-title {
    height: 48px; background: var(--brand-blue); color: #fff;
    font-family: "Montserrat", sans-serif; font-weight: 800;
    font-size: 23px; letter-spacing: .5px;
    display: flex; align-items: center; justify-content: center;
  }
  .front-tagline {
    text-align: center; font-size: 16px; line-height: 20px;
    margin-top: 5px; color: #666;
  }
  .front-footer-band {
    position: absolute; left: 0; right: 0; bottom: 0; height: 72px;
    background: var(--brand-blue);
  }
  .front-footer-text {
    position: absolute; left: 0; right: 0; bottom: 16px;
    text-align: center; color: #fff; font-size: 17px;
  }
  .service-table {
    position: absolute; left: 20px; top: 99px; width: 801px;
    display: grid; grid-template-columns: 1fr 1fr; column-gap: 3px;
    background: var(--card-white); z-index: 1;
  }
  .table-col { display: flex; flex-direction: column; }
  .col-head {
    height: 33px; display: flex; align-items: center; justify-content: center;
    font-family: "Montserrat", sans-serif; font-weight: 700; font-size: 20px;
    letter-spacing: .5px;
  }
  .col-head.light { background: var(--head-light); color: var(--head-text); }
  .col-head.dark { background: var(--head-dark); color: #fff; }
  .col-head.plain { background: var(--row-tint); color: var(--head-text); height: 41px; }
  .item {
    display: flex; align-items: center; gap: 9px;
    padding: 0 10px; font-size: 12.6px; line-height: 15px;
    border-bottom: 1px solid var(--rule);
  }
  .item:nth-child(odd) { background: var(--row-tint); }
  .item.blank { border-bottom: none; background: var(--row-tint); }

  .tick {
    flex: none; width: 10px; height: 10px; background: var(--brand-blue);
    position: relative; align-self: flex-start; margin-top: 3px;
  }
  .tick::after {
    content: ""; position: absolute; left: 3px; top: 1px;
    width: 3px; height: 5px; border: solid #fff; border-width: 0 1.5px 1.5px 0;
    transform: rotate(45deg);
  }

  /* back */
  .back-title {
    position: absolute; left: 20px; top: 22px; width: 389px; height: 82px;
    background: var(--brand-blue); color: #fff;
    font-family: "Montserrat", sans-serif; font-weight: 800;
    font-size: 22px; line-height: 25px; letter-spacing: .5px;
    padding: 14px 20px;
  }
  .stamp-box {
    position: absolute; left: 696px; top: 22px; width: 119px; height: 119px;
    background: var(--stamp);
  }
  .address-line {
    position: absolute; left: 474px; width: 341px; height: 1px; background: var(--rule);
  }
  .back-benefits {
    position: absolute; left: 34px; top: 120px; width: 370px;
    list-style: none; display: flex; flex-direction: column; gap: 12px;
  }
  .back-benefits li {
    display: flex; gap: 11px; font-size: 12.4px; line-height: 14.5px;
  }
  .back-contact {
    position: absolute; left: 20px; top: 436px; width: 389px; height: 103px;
    background: var(--brand-blue); color: #fff; padding: 10px 0 0 10px;
  }
  .phone-row { display: flex; align-items: center; gap: 8px; }
  .phone-number {
    font-family: "Montserrat", sans-serif; font-weight: 800;
    font-size: 45px; line-height: 52px; letter-spacing: 1px;
  }
  .web-row {
    display: flex; align-items: center; gap: 14px; margin-left: 4px;
    font-family: "Montserrat", sans-serif; font-weight: 700; font-size: 18px;
  }
</style>
</head>
<body>

<section class="postcard postcard-front" aria-label="Postcard front">
  <h1 class="front-title">WEXLEY RESIDENTIAL MANAGEMENT LLC (WRM)</h1>
  <p class="front-tagline">Improve compliance, reporting, and communication amongst<br>all owners and board members</p>

  <div class="service-table">
    <div class="table-col">
      <h2 class="col-head light">WHO WE ARE</h2>
      <div class="item" style="height:51px"><span class="tick"></span>A professional services organization with a focus on small (3-10 unit) residential buildings</div>
      <div class="item" style="height:53px"><span class="tick"></span>Over 30 years of combined experience in real estate and property management</div>
      <div class="item" style="height:50px"><span class="tick"></span>Professional, courteous, timely service that is technologically driven</div>
      <h2 class="col-head plain">WHY USE WRM?</h2>
      <div class="item" style="height:64px"><span class="tick"></span>Owners are rarely suited to manage associations and the burden often falls unfairly on one or two individuals to do all the work</div>
      <div class="item" style="height:34px"><span class="tick"></span>Low monthly fees tailored to your needs</div>
      <div class="item" style="height:48px"><span class="tick"></span>The association’s board of directors maintains control of all decision making</div>
      <div class="item blank" style="height:41px"></div>
    </div>
    <div class="table-col">
      <h2 class="col-head dark">WHAT WE DO</h2>
      <div class="item" style="height:51px"><span class="tick"></span>Remove the administrative burden of managing small residential buildings</div>
      <div class="item" style="height:53px"><span class="tick"></span>Utilize economies of scale to reduce expenses for all owners across a wide variety of service providers</div>
      <div class="item" style="height:50px"><span class="tick"></span>Collect all assessments and pay all bills</div>
      <div class="item" style="height:41px"><span class="tick"></span>Provide monthly accounting reconciliation and reporting</div>
      <div class="item" style="height:64px"><span class="tick"></span>Provide access to WRM’s client portal with a central repository of all association materials (bylaws, financials, meeting minutes, communications, etc)</div>
      <div class="item" style="height:38px"><span class="tick"></span>Issue 1099s to all contractors as required by law</div>
      <div class="item" style="height:38px"><span class="tick"></span>Prepare year-end financial statements</div>
      <div class="item" style="height:47px;border-bottom:none"><span class="tick"></span>Lender and legal HOA documents for mortgage companies and sales</div>
    </div>
  </div>

  <div class="front-footer-band"></div>
  <p class="front-footer-text">www.wexleymanagement.com I 312-555-0187</p>
</section>

<section class="postcard postcard-back" aria-label="Postcard back">
  <h2 class="back-title">WEXLEY RESIDENTIAL<br>MANAGEMENT LLC (WRM)</h2>
  <div class="stamp-box"></div>
  <div class="address-line" style="top:194px"></div>
  <div class="address-line" style="top:305px"></div>

  <ul class="back-benefits">
    <li><span class="tick"></span>Cost effective property management solution for 3-10 unit buildings</li>
    <li><span class="tick"></span>Prices starting as low as $100/month</li>
    <li><span class="tick"></span>Utilize our economies of scale to reduce costs across existing services (trash, insurance, maintenance, etc)</li>
    <li><span class="tick"></span>Eliminate the unfair burden placed on a few owners to do all the work while others free-ride</li>
    <li><span class="tick"></span>Improve communication amongst all owners and board members</li>
    <li><span class="tick"></span>The association’s board of directors maintain all decision-making power</li>
    <li><span class="tick"></span>Utilize our vetted service providers for prompt job completion and fair pricing</li>
  </ul>

  <div class="back-contact">
    <div class="phone-row">
      <svg width="26" height="30" viewBox="0 0 26 30" aria-hidden="true">
        <rect x="1" y="1" width="24" height="28" rx="5" fill="#fff"/>
        <path d="M9 6c-2 1-3 3-2.5 6 .6 4 3 8 6.5 11 2 1.6 4 1.5 5.5.5l-2.5-4-2 1c-1.5-1.5-3-4-3.5-6l2-1.2L10.5 6z" fill="var(--brand-blue)"/>
      </svg>
      <span class="phone-number">312-555-0187</span>
    </div>
    <div class="web-row">
      <svg width="14" height="14" viewBox="0 0 14 14" aria-hidden="true" fill="none" stroke="#fff" stroke-width="1.1">
        <circle cx="7" cy="7" r="6"/><ellipse cx="7" cy="7" rx="2.6" ry="6"/><path d="M1 7h12M2 4h10M2 10h10"/>
      </svg>
      <span>www.wexleymanagement.com</span>
    </div>
  </div>
</section>

</body>
</html>
```